BKA

Please send us some options for letterhead I attached our Logo. In addition to the Logo we need this information somewhere on the page

47 Fenbury Lane
Millbrook, CT 06712
203-481-7629

```html
<!DOCTYPE html>
<html lang="en">
<head>
<meta charset="utf-8">
<title>BKA Letterhead</title>
<link href="https://fonts.googleapis.com/css2?family=Arimo:wght@400;700&display=swap" rel="stylesheet">
<style>
  :root {
    --paper: #ffffff;
    --ink-dark: #2b2527;
    --ink-grey: #58585a;
    --rule-grey: #6d6e70;
    --accent-blue: #2aa9e0;
  }
  * { margin: 0; padding: 0; box-sizing: border-box; }
  html, body {
    width: 927px;
    height: 1200px;
    overflow: hidden;
    background: var(--paper);
  }
  .letterhead {
    position: relative;
    width: 927px;
    height: 1200px;
    background: var(--paper);
    font-family: "Arimo", Arial, sans-serif;
  }
  .brand {
    position: absolute;
    left: 40px;
    top: 38px;
    display: flex;
    align-items: center;
    gap: 18px;
  }
  .brand-square {
    width: 80px;
    height: 80px;
    background: var(--accent-blue);
  }
  .brand-name {
    font-size: 50px;
    font-weight: 700;
    color: var(--ink-dark);
    letter-spacing: 1px;
    line-height: 1;
  }
  .contact {
    position: absolute;
    right: 44px;
    top: 56px;
    text-align: right;
    font-size: 17px;
    line-height: 20.5px;
    color: var(--ink-grey);
    font-style: normal;
  }
  .footer {
    position: absolute;
    left: 34px;
    right: 30px;
    top: 1150px;
    display: flex;
    align-items: center;
    gap: 22px;
  }
  .footer-rule {
    flex: 1;
    height: 1px;
    background: var(--rule-grey);
  }
  .footer-web {
    font-size: 17px;
    color: var(--ink-grey);
    white-space: nowrap;
  }
</style>
</head>
<body>
  <main class="letterhead">
    <header class="brand">
      <div class="brand-square" aria-hidden="true"></div>
      <span class="brand-name">BKA</span>
    </header>

    <address class="contact">
      47 Fenbury Lane<br>
      Millbrook, CT 06712<br>
      203-481-7629
    </address>

    <footer class="footer">
      <span class="footer-rule"></span>
      <span class="footer-web">www.bkahomelending.com</span>
      <span class="footer-rule"></span>
    </footer>
  </main>
</body>
</html>
```